Become a Mentor - For Musicians, Artists, Producers and Teachers

Here is the full creative brief:

https://files.plenwick.com/sheets/d/4kTqpLm8Wz_2RNa7Hc3Xv91Jd0Gb5YeUsQ6fNo8rTpxa/view?mode=shared

Here is the background image file: https://www.trovecrate.com/sh/83jbwtrmq5dkx2u/BBHn4k7QTf2ZpLeXX-wr9MUHe?dl=0

LOGO:
https://www.trovecrate.com/sh/k472rufmpdo9b6w/BBKLe3RtHY5J-sFQnLZw7Ggma?dl=0

```html
<!DOCTYPE html>
<html lang="en">
<head>
<meta charset="utf-8">
<title>Become a Mentor – Meridian Sound Academy</title>
<link rel="stylesheet" href="https://fonts.googleapis.com/css2?family=Oswald:wght@700&family=Playball&family=Roboto:wght@500;700&display=swap">
<style>
  :root {
    --page: #ffffff;
    --sky: #1089e3;
    --ocean: #0b4f93;
    --navy: #0a2a52;
    --ink: #000000;
    --cream: #f2dfba;
    --gold-light: #fbf3e4;
    --gold: #d8bd8c;
    --gold-deep: #b89a66;
    --white: #ffffff;
    --type-navy: #0b1f3a;
  }
  * { margin: 0; padding: 0; box-sizing: border-box; }
  html, body {
    width: 1200px; height: 1200px; overflow: hidden;
    background: var(--page);
  }
  .flyer {
    position: absolute; left: 200px; top: 33px;
    width: 800px; height: 1134px; overflow: hidden;
    background: linear-gradient(180deg, var(--sky) 0%, var(--ocean) 45%, var(--navy) 62%, var(--ink) 82%, var(--ink) 100%);
  }
  .flyer-art { position: absolute; inset: 0; }
  .apply-badge {
    position: absolute; left: 35px; top: 379px;
    width: 220px; height: 220px; border-radius: 50%;
    background: radial-gradient(circle at 35% 30%, var(--gold-light), var(--gold) 60%, var(--gold-deep));
    box-shadow: inset 0 0 0 22px rgba(255,255,255,0.18);
    display: flex; align-items: center; justify-content: center;
  }
  .apply-badge span {
    display: block; transform: rotate(-20deg);
    font-family: "Oswald", sans-serif; font-weight: 700;
    color: var(--navy); text-align: center;
    font-size: 48px; line-height: 0.95;
  }
  .apply-badge span em { font-style: normal; font-size: 40px; }
  .headline {
    position: absolute; right: 81px; top: 338px;
    text-align: right;
  }
  .headline h1 {
    font-family: "Oswald", sans-serif; font-weight: 700;
    font-size: 50px; line-height: 1.1; color: var(--cream);
    letter-spacing: -0.5px;
    text-shadow: 0 2px 6px rgba(0,0,0,0.45);
  }
  .headline p {
    font-family: "Playball", cursive;
    font-size: 42px; line-height: 1; color: var(--white);
    margin-top: -6px;
    text-shadow: 0 2px 6px rgba(0,0,0,0.5);
  }
  .tagline {
    position: absolute; left: 59px; top: 648px;
    font-family: "Playball", cursive;
    font-size: 40px; line-height: 36px; color: var(--white);
  }
  .contact-phone {
    position: absolute; left: 60px; top: 754px;
    display: flex; align-items: center; gap: 20px;
  }
  .contact-phone .icon {
    width: 56px; height: 56px; border-radius: 50%;
    background: radial-gradient(circle at 35% 30%, var(--gold-light), var(--gold) 70%);
    display: flex; align-items: center; justify-content: center;
  }
  .contact-phone .number {
    font-family: "Oswald", sans-serif; font-weight: 700;
    font-size: 34px; color: var(--cream); letter-spacing: -0.5px;
  }
  .audience {
    position: absolute; right: 78px; top: 812px; text-align: right;
  }
  .audience h2 {
    font-family: "Oswald", sans-serif; font-weight: 700;
    font-size: 34px; line-height: 1.2; color: var(--cream);
    margin-bottom: 8px;
  }
  .audience ul { list-style: none; }
  .audience li {
    font-family: "Roboto", sans-serif; font-weight: 500;
    font-size: 26px; line-height: 33px; color: var(--white);
  }
  .brand {
    position: absolute; left: 50px; top: 905px;
    display: flex; align-items: center; gap: 12px;
  }
  .brand .mark {
    width: 18px; height: 18px; border-radius: 50%; background: var(--white);
  }
  .brand .name {
    font-family: "Roboto", sans-serif; font-weight: 700;
    font-size: 24px; line-height: 1.1; color: var(--white);
    text-transform: uppercase; letter-spacing: 1px;
  }
  .footer-band {
    position: absolute; left: 0; right: 0; bottom: 0; height: 90px;
    background: linear-gradient(90deg, var(--gold) 0%, var(--gold-light) 35%, var(--gold) 60%, var(--gold-light) 85%, var(--gold) 100%);
  }
  .footer-tab {
    position: absolute; left: 336px; top: 980px;
    width: 128px; height: 128px; border-radius: 50%;
    background: linear-gradient(180deg, var(--gold-light), var(--gold));
  }
  .footer-tab svg { position: absolute; left: 28px; top: 30px; }
  .website {
    position: absolute; left: 0; right: 0; top: 1070px;
    text-align: center;
    font-family: "Roboto", sans-serif; font-weight: 500;
    font-size: 29px; color: var(--type-navy); letter-spacing: 0.3px;
  }
</style>
</head>
<body>
  <main class="flyer">
    <svg class="flyer-art" width="800" height="1134" viewBox="0 0 800 1134">
      <defs>
        <linearGradient id="studio-tones" x1="0" y1="0" x2="1" y2="1">
          <stop offset="0" stop-color="#8a7462"/>
          <stop offset="0.45" stop-color="#6d6a6c"/>
          <stop offset="1" stop-color="#3a3336"/>
        </linearGradient>
        <linearGradient id="gold-line" x1="0" y1="0" x2="1" y2="0">
          <stop offset="0" stop-color="#f6e8cf"/>
          <stop offset="1" stop-color="#d3b585"/>
        </linearGradient>
      </defs>
      <path role="img" aria-label="Photo: two young music producers talking at a mixing desk in a recording studio"
            d="M0,0 H290 C560,20 770,260 800,640 C640,580 420,520 260,500 C130,470 40,380 0,270 Z"
            fill="url(#studio-tones)"/>
      <path d="M300,12 C560,40 760,270 800,600" fill="none" stroke="url(#gold-line)" stroke-width="7"/>
      <path d="M440,0 C620,40 780,200 800,360" fill="none" stroke="url(#gold-line)" stroke-width="5"/>
      <path d="M0,290 C40,390 140,470 270,510 C440,540 600,580 710,620" fill="none" stroke="url(#gold-line)" stroke-width="5"/>
    </svg>

    <div class="apply-badge"><span>APPLY<br><em>NOW!!</em></span></div>

    <header class="headline">
      <h1>Start Your Career Today</h1>
      <p>Become a Mentor</p>
    </header>

    <p class="tagline">Turn your skills and passion<br>for music into a career!!</p>

    <div class="contact-phone">
      <div class="icon">
        <svg width="28" height="28" viewBox="0 0 24 24" aria-hidden="true">
          <path fill="#0a2a52" d="M6.6 10.8c1.4 2.8 3.8 5.1 6.6 6.6l2.2-2.2c.3-.3.7-.4 1-.2 1.1.4 2.3.6 3.6.6.6 0 1 .4 1 1V20c0 .6-.4 1-1 1C10.6 21 3 13.4 3 4c0-.6.4-1 1-1h3.5c.6 0 1 .4 1 1 0 1.3.2 2.5.6 3.6.1.3 0 .7-.2 1z"/>
        </svg>
      </div>
      <span class="number">1300 - 555 - 018</span>
    </div>

    <section class="audience">
      <h2>Designed for:</h2>
      <ul>
        <li>Musicians</li>
        <li>Artists</li>
        <li>Producers</li>
        <li>&amp; Teachers</li>
      </ul>
    </section>

    <div class="brand">
      <span class="mark"></span>
      <span class="name">Meridian<br>Sound Academy</span>
    </div>

    <div class="footer-tab">
      <svg width="72" height="48" viewBox="0 0 72 48" aria-hidden="true">
        <rect x="0" y="0" width="72" height="48" rx="3" fill="#0a2a52"/>
        <path d="M2,2 L36,28 L70,2" fill="none" stroke="#dfe3ea" stroke-width="4"/>
      </svg>
    </div>
    <div class="footer-band"></div>
    <p class="website">www.meridiansoundacademy.com.au</p>
  </main>
</body>
</html>
```